Redesigning a sales pitch ppt document

This document is to be used as a sales-pitch - for an initial meeting with prospective clients.

Challenge is the document is rather boring graphically - formatting is in business consulting style, versus a more interesting sales brochure.

We will like to change the document to be much more fun, while being classic given that we are in the busines of selling experiential gifts. We will like to portray an image of a company that is fun, pioneering (we are one of the few companies doing experiential gifts in China), but at the same time, being very tasteful.

There are some Chinese words in the document but feel free to ignore as it should not impat the storyline.

What we are looking for:
- Re-do the ppt so it can have a new look and feel that portrays the above
- Have a ppt template for future documents

Note:
- We like the feel of the cover page - so we keep it in its current form though of course, happy to change fonts etc.
- All the other pages we can change.

Have attached the following:

1. current version of the file translated into English.
2. What some of the competitors do (the Lumo-Tine file) - but believe that this is too flashy and we are looking for something more tasteful and classy (though still have to be portrayed as cool and pioneering

For more information about the parent company (this business is a standalone subsidiary), you can visit www.farbrookvale.com and www.tarimov.com

Target Market(s)

China, Corporates - mostly in professional service and tech sector

Industry/Entity Type

Sales

Requirements
Must have
• Revised PPT with updated format
• Revised template
Nice to have
• Should be cool, pioneering while also showing the classy, heritage look as our gifts are classy but the idea of giving experiential gifts is pioneering (at least in China)
Should not have
• Am open to other fonts except for Sans Seirf

```html
<!DOCTYPE html>
<html lang="en">
<head>
<meta charset="utf-8">
<title>LUMARO gift – Sales Pitch Deck</title>
<link rel="stylesheet" href="https://fonts.googleapis.com/css2?family=Montserrat:wght@400;600;700&family=Noto+Sans+SC:wght@400;700&family=Raleway:wght@300;400;600&display=swap">
<style>
:root{
  --orange:#f07d1a;
  --navy:#1c3349;
  --grey:#7d7d7d;
  --grey-light:#d9d9d9;
  --grey-mid:#8a8a8a;
  --ink:#222;
  --white:#fff;
}
*{box-sizing:border-box;margin:0;padding:0}
html,body{width:1200px;height:3000px;overflow:hidden;background:var(--white)}
body{position:relative;font-family:"Montserrat","Noto Sans SC",sans-serif;color:var(--ink)}

.slide{position:absolute;width:582px;height:440px;background:var(--white);box-shadow:0 2px 9px rgba(0,0,0,.2);overflow:hidden}
.col-l{left:14px}.col-r{left:606px}
.row-1{top:28px}.row-2{top:528px}.row-3{top:1032px}.row-4{top:1532px}.row-5{top:2032px}.row-6{top:2532px}

.slide-title{position:absolute;left:28px;top:24px;font-family:"Raleway",sans-serif;font-weight:400;font-size:38px;color:var(--navy);line-height:1.1}
.slide-title::after{content:"";position:absolute;left:2px;bottom:-10px;width:36px;height:3px;background:var(--orange)}
.slide-title--small{font-size:28px;top:30px}

.footer-brand{position:absolute;left:28px;top:404px;font-family:"Montserrat",sans-serif;font-weight:700;font-size:12px;letter-spacing:.5px;color:var(--navy)}
.page-num{position:absolute;right:40px;top:404px;font-size:9px;color:var(--ink)}

/* cover */
.cover-photo{position:absolute;left:0;top:0;width:582px;height:360px;
  background:
   radial-gradient(ellipse 140px 70px at 30% 52%,rgba(230,215,60,.85),transparent 70%),
   radial-gradient(ellipse 120px 60px at 75% 48%,rgba(238,140,180,.8),transparent 70%),
   radial-gradient(ellipse 100px 50px at 55% 40%,rgba(120,200,220,.6),transparent 70%),
   linear-gradient(180deg,#7fa6d8 0%,#9cbde0 25%,#c8d35a 48%,#e094a6 62%,#4a3a34 80%,#231d1c 100%)}
.cover-band{position:absolute;left:0;top:360px;width:582px;height:80px;background:var(--grey-light)}
.cover-brand{position:absolute;font-family:"Montserrat",sans-serif;font-weight:700;font-size:30px;color:var(--white);letter-spacing:1px}
.cover-tagline{position:absolute;font-family:"Noto Sans SC",sans-serif;font-size:12px;color:var(--white)}
.cover-headline{position:absolute;font-family:"Noto Sans SC",sans-serif;font-size:25px;line-height:47px;color:var(--white);text-align:center}
.cover-disclaimer{position:absolute;font-size:9.5px;line-height:12px;color:var(--ink)}
.cover-brand-box{position:absolute;left:24px;top:0;width:146px;height:140px;background:var(--orange)}
.parent-mark{position:absolute;writing-mode:vertical-rl;font-family:"Montserrat",sans-serif;font-weight:700;font-size:8px;letter-spacing:1px;text-align:center}
.parent-mark--plain{left:536px;top:372px;height:62px;width:26px;color:var(--orange)}
.parent-mark--box{left:532px;top:372px;width:34px;height:62px;background:var(--orange);color:var(--white);line-height:34px}

/* agenda */
.agenda-list{position:absolute;left:24px;top:148px;list-style:none}
.agenda-item{display:flex;align-items:center;height:52px;font-size:17px;font-weight:600;color:var(--grey)}
.agenda-num{display:inline-flex;align-items:center;justify-content:center;width:26px;height:26px;border-radius:50%;background:#a6a6a6;color:var(--white);font-size:13px;font-weight:600;margin-right:14px}
.agenda-item--active{color:var(--navy);font-weight:700}
.agenda-item--active .agenda-num{background:var(--navy);box-shadow:0 0 0 3px var(--white),0 0 0 5px var(--orange)}

/* galleries */
.photo{position:absolute;overflow:hidden}
.photo-caption{position:absolute;left:0;right:0;bottom:0;font-size:9px;line-height:12px;padding:6px 8px}
.photo-caption--light{background:rgba(255,255,255,.82);color:var(--ink);height:38px}
.photo-caption--orange{background:var(--orange);color:var(--white);height:48px;padding-top:10px;font-weight:600}

/* navy panels */
.navy-panel{position:absolute;left:0;top:0;height:440px;background:var(--navy)}
.solve-heading{position:absolute;right:350px;top:222px;width:200px;text-align:right;font-family:"Raleway",sans-serif;font-size:25px;line-height:30px;color:#e8e8e8}
.solve-item{position:absolute;left:286px;width:240px;font-size:15px;line-height:20px;color:var(--navy);font-family:"Raleway",sans-serif}
.solve-icon{display:block;margin-bottom:8px}

.challenge-intro{position:absolute;left:28px;top:74px;width:526px;font-size:10px;line-height:15px;color:var(--grey)}
.diagram{position:absolute;left:0;top:0}

.trend-title{position:absolute;left:230px;top:16px;font-family:"Raleway",sans-serif;font-size:22px;line-height:26px;color:var(--navy)}
.trend-title::after{content:"";position:absolute;left:2px;bottom:-6px;width:32px;height:3px;background:var(--orange)}
.trend-sub{position:absolute;left:260px;top:82px;width:270px;text-align:center;font-size:10.5px;color:var(--navy)}
.occasion{position:absolute;font-size:7.5px;line-height:9.5px;color:var(--grey)}
.occasion h4{font-size:9px;color:var(--orange);font-weight:700;margin-bottom:2px}
.occasion--right-align{text-align:right}
.panel-stat-title{position:absolute;left:16px;top:76px;width:176px;text-align:center;color:#dfe4ea;font-size:10.5px;line-height:14px}
.panel-photo{position:absolute;left:0;top:360px;width:208px;height:80px;background:linear-gradient(180deg,rgba(28,51,73,0),#33485e)}
</style>
</head>
<body>

<!-- Cover A -->
<section class="slide col-l row-1">
  <div class="cover-photo" role="img" aria-label="Festival crowd throwing clouds of yellow, pink and blue colour powder under a blue sky"></div>
  <div class="cover-brand" style="left:28px;top:18px">LUMARO . gift</div>
  <div class="cover-tagline" style="left:30px;top:62px">专注精选体验式的礼品电商</div>
  <div class="cover-headline" style="left:120px;top:112px;width:360px">帮助企业一站式完美解决<br>员工个性化奖励<br>差异化客户礼品</div>
  <div class="cover-band"></div>
  <p class="cover-disclaimer" style="left:244px;top:374px;width:272px">This report is solely for the use of client personnel. No part of it may be circulated, quoted, or reproduced for distribution outside the client organization without prior written approval from Farbrookvale Company Limited.</p>
  <div class="parent-mark parent-mark--plain">FARBROOKVALE</div>
</section>

<!-- Cover B -->
<section class="slide col-r row-1">
  <div class="cover-photo" role="img" aria-label="Festival crowd throwing clouds of yellow, pink and blue colour powder under a blue sky"></div>
  <div class="cover-brand-box"></div>
  <div class="cover-brand" style="left:46px;top:48px">LUMARO . gift</div>
  <div class="cover-tagline" style="left:46px;top:92px">专注精选体验式的礼品电商</div>
  <div class="cover-headline" style="left:220px;top:140px;width:360px">帮助企业一站式完美解决<br>员工个性化奖励<br>差异化客户礼品</div>
  <div class="cover-band"></div>
  <p class="cover-disclaimer" style="left:24px;top:380px;width:400px;color:var(--orange)">This report is solely for the use of client personnel. No part of it may be circulated, quoted, or reproduced for distribution outside the client organization without prior written approval from Farbrookvale Company Limited.</p>
  <div class="parent-mark parent-mark--box">FARBROOKVALE</div>
</section>

<!-- Agenda 1 -->
<section class="slide col-l row-2">
  <h2 class="slide-title">Agenda</h2>
  <ol class="agenda-list">
    <li class="agenda-item agenda-item--active"><span class="agenda-num">1</span>Our Products</li>
    <li class="agenda-item"><span class="agenda-num">2</span>Your Challenges</li>
    <li class="agenda-item"><span class="agenda-num">3</span>How we can help?</li>
  </ol>
  <div class="footer-brand">LUMARO . gift</div>
  <div class="page-num">2</div>
</section>

<!-- Adventure -->
<section class="slide col-r row-2">
  <h2 class="slide-title slide-title--small">Lumaro Experiential Gifts Adventure</h2>
  <div class="photo" style="left:20px;top:112px;width:180px;height:240px;background:linear-gradient(180deg,#e0d9cf,#b08a66 60%,#7a5236)" role="img" aria-label="Helicopter landing on a rocky hillside">
    <p class="photo-caption photo-caption--light">¥2000 | Helicopter ride over the Great Wall.</p></div>
  <div class="photo" style="left:206px;top:112px;width:176px;height:240px;background:linear-gradient(180deg,#4a7fb0,#6f6a5e 55%,#7a5a3c)" role="img" aria-label="Climber reaching for a partner's hand on a rock face">
    <p class="photo-caption photo-caption--light">¥328 | Rock climbing with a pro guide.</p></div>
  <div class="photo" style="left:388px;top:112px;width:176px;height:240px;background:linear-gradient(180deg,#cfcac4,#b22a1e 60%,#5a1a14)" role="img" aria-label="Red racing car on a track">
    <p class="photo-caption photo-caption--light">¥2322 | Drive a race car on a real track.</p></div>
  <div class="footer-brand">LUMARO . gift</div>
  <div class="page-num">3</div>
</section>

<!-- Gourmet -->
<section class="slide col-l row-3">
  <h2 class="slide-title">Gourmet</h2>
  <div class="photo" style="left:4px;top:84px;width:188px;height:308px;background:linear-gradient(180deg,#8a7a6c,#6a5548 45%,#a33a26)" role="img" aria-label="Couple standing at the red door of a traditional courtyard house">
    <p class="photo-caption photo-caption--orange">¥1600 | Dine at a hidden courtyard with a local chef.</p></div>
  <div class="photo" style="left:198px;top:84px;width:184px;height:308px;background:linear-gradient(180deg,#7a5a3e,#5a3e2a 50%,#2e241d)" role="img" aria-label="Hands cooking over an open wood fire outdoors">
    <p class="photo-caption photo-caption--orange">¥200 | Cook over open fire in a village kitchen (8 pax).</p></div>
  <div class="photo" style="left:388px;top:84px;width:190px;height:308px;background:linear-gradient(180deg,#9a7a5e,#6b4e3a 50%,#3a2b22)" role="img" aria-label="Chef in a cap plating food in a kitchen">
    <p class="photo-caption photo-caption--orange">¥328 | Learn plating from a top chef in his own studio.</p></div>
  <div class="footer-brand">LUMARO . gift</div>
  <div class="page-num">4</div>
</section>

<!-- Pampering -->
<section class="slide col-r row-3">
  <h2 class="slide-title">Pampering</h2>
  <div class="photo" style="left:24px;top:112px;width:172px;height:248px;background:linear-gradient(180deg,#d9a07a,#a8674a 55%,#5a3522)" role="img" aria-label="Woman relaxing during a spa treatment">
    <p class="photo-caption photo-caption--light">¥720 | Ninety minutes of spa care in a quiet garden retreat.</p></div>
  <div class="photo" style="left:204px;top:112px;width:176px;height:248px;background:linear-gradient(180deg,#3f78bc,#6fa0d6 55%,#b8d2ea)" role="img" aria-label="Woman in a yoga pose against a blue sky">
    <p class="photo-caption photo-caption--light">¥300 | Sunrise yoga on a city rooftop for two.</p></div>
  <div class="photo" style="left:388px;top:112px;width:176px;height:248px;background:linear-gradient(180deg,#f1d8a0,#c9a272 45%,#2c2a34)" role="img" aria-label="Silhouette in a meditation pose at sunset">
    <p class="photo-caption photo-caption--light">¥300 | Guided meditation at dusk by the lake.</p></div>
  <div class="footer-brand">LUMARO . gift</div>
  <div class="page-num">5</div>
</section>

<!-- Culture -->
<section class="slide col-l row-4">
  <h2 class="slide-title">Culture</h2>
  <div class="photo" style="left:4px;top:84px;width:188px;height:308px;background:linear-gradient(180deg,#8a9476,#6a6a56 45%,#4a4038)" role="img" aria-label="Two travellers standing with a horse outdoors">
    <p class="photo-caption photo-caption--orange">¥1600 | Ride with herders through the grasslands.</p></div>
  <div class="photo" style="left:198px;top:84px;width:184px;height:308px;background:linear-gradient(180deg,#e2dbd0,#b8a896 55%,#8c7a68)" role="img" aria-label="Hand writing calligraphy on paper">
    <p class="photo-caption photo-caption--orange">¥300 | Calligraphy lesson with a master, for one.</p></div>
  <div class="photo" style="left:388px;top:84px;width:190px;height:308px;background:linear-gradient(180deg,#8a939c,#5a6470 50%,#2a3038)" role="img" aria-label="Palace corner tower reflected in a moat at dusk">
    <p class="photo-caption photo-caption--orange">¥200 | Palace tour at dawn before the crowds arrive.</p></div>
  <div class="footer-brand">LUMARO . gift</div>
  <div class="page-num">6</div>
</section>

<!-- Staycations -->
<section class="slide col-r row-4">
  <h2 class="slide-title">Staycations</h2>
  <div class="photo" style="left:24px;top:116px;width:172px;height:232px;background:linear-gradient(180deg,#dfe3e8,#aab5c0 55%,#8a97a3)" role="img" aria-label="Hotel room window overlooking a city harbour">
    <p class="photo-caption photo-caption--light">¥3680/3 | Harbour view suite for two nights.</p></div>
  <div class="photo" style="left:204px;top:116px;width:176px;height:232px;background:linear-gradient(180deg,#2d4870,#24344a 55%,#1a2430)" role="img" aria-label="Lit hillside villa among trees at night">
    <p class="photo-caption photo-caption--light">¥1500 | Hillside villa weekend with breakfast.</p></div>
  <div class="photo" style="left:388px;top:116px;width:176px;height:232px;background:linear-gradient(180deg,#1e3a7a,#3e4a8a 55%,#6a4a8a)" role="img" aria-label="Illuminated fairytale castle against a night sky">
    <p class="photo-caption photo-caption--light">¥5000 | Family stay at the castle resort park.</p></div>
  <div class="footer-brand">LUMARO . gift</div>
  <div class="page-num">7</div>
</section>

<!-- Agenda 2 -->
<section class="slide col-l row-5">
  <h2 class="slide-title">Agenda</h2>
  <ol class="agenda-list">
    <li class="agenda-item"><span class="agenda-num">1</span>Our Products</li>
    <li class="agenda-item agenda-item--active"><span class="agenda-num">2</span>Your Challenges</li>
    <li class="agenda-item"><span class="agenda-num">3</span>How we can help?</li>
  </ol>
  <div class="footer-brand">LUMARO . gift</div>
  <div class="page-num">8</div>
</section>

<!-- What we solve -->
<section class="slide col-r row-5">
  <div class="navy-panel" style="width:240px"></div>
  <p class="solve-heading">Our experiential gifts can help solve:</p>
  <div class="solve-item" style="top:70px">
    <svg class="solve-icon" width="30" height="30" viewBox="0 0 30 30"><circle cx="15" cy="15" r="13" fill="none" stroke="var(--orange)" stroke-width="1.5"/><circle cx="15" cy="15" r="7" fill="none" stroke="var(--navy)" stroke-width="1.2"/><path d="M15 11v8M12.5 13h4a1.5 1.5 0 0 1 0 3h-3a1.5 1.5 0 0 0 0 3h4" fill="none" stroke="var(--navy)" stroke-width="1"/></svg>
    Lowers overall cost
  </div>
  <div class="solve-item" style="top:168px">
    <svg class="solve-icon" width="30" height="30" viewBox="0 0 30 30"><circle cx="15" cy="15" r="13" fill="none" stroke="var(--orange)" stroke-width="1.5"/><circle cx="11" cy="12" r="2.5" fill="none" stroke="var(--navy)" stroke-width="1.2"/><circle cx="19" cy="12" r="2.5" fill="none" stroke="var(--navy)" stroke-width="1.2"/><path d="M6.5 21a4.5 4.5 0 0 1 9 0M14.5 21a4.5 4.5 0 0 1 9 0" fill="none" stroke="var(--navy)" stroke-width="1.2"/></svg>
    More effectively engage and motivate customers and staff
  </div>
  <div class="solve-item" style="top:282px">
    <svg class="solve-icon" width="30" height="30" viewBox="0 0 30 30"><circle cx="15" cy="15" r="13" fill="none" stroke="var(--orange)" stroke-width="1.5"/><circle cx="15" cy="12" r="5" fill="none" stroke="var(--navy)" stroke-width="1.2"/><path d="M12 16.5l-2 6 3-1.5 2 2M18 16.5l2 6-3-1.5-2 2" fill="none" stroke="var(--navy)" stroke-width="1.2"/></svg>
    Create a recognition culture within the company
  </div>
  <div class="page-num" style="color:var(--grey)">9</div>
</section>

<!-- Current challenges -->
<section class="slide col-l row-6">
  <h2 class="slide-title" style="font-size:34px;top:14px">Current challenges</h2>
  <p class="challenge-intro">Like pay, rewards must meet every level of need. Beyond cash, curated experiences build loyalty, lift motivation and make a gift truly memorable.</p>
  <svg class="diagram" width="582" height="440" viewBox="0 0 582 440" font-family="Noto Sans SC, Montserrat, sans-serif">
    <g stroke="#fff" stroke-width="2">
      <polygon points="190,160 219.7,208 160.3,208" fill="var(--orange)"/>
      <polygon points="160.3,208 219.7,208 245.7,250 134.3,250" fill="var(--orange)"/>
      <polygon points="134.3,250 245.7,250 270.5,290 109.5,290" fill="var(--navy)"/>
      <polygon points="109.5,290 270.5,290 295.2,330 84.8,330" fill="var(--grey-mid)"/>
      <polygon points="84.8,330 295.2,330 320,370 60,370" fill="var(--orange)"/>
    </g>
    <g fill="#fff" font-weight="700" text-anchor="middle">
      <text x="190" y="192" font-size="9">自我</text><text x="190" y="203" font-size="9">实现</text>
      <text x="190" y="234" font-size="13">尊重需求</text>
      <text x="190" y="275" font-size="13">爱的需求</text>
      <text x="190" y="315" font-size="13">安全需求</text>
      <text x="190" y="355" font-size="13">生理需求</text>
    </g>
    <g font-size="11" fill="var(--grey-mid)">
      <text x="236" y="190">道德，创造力，公正</text>
      <text x="258" y="234" fill="var(--orange)">尊重，信心，成就</text>
      <text x="283" y="275">归属，友情，爱情</text>
      <text x="308" y="315">安全，健康，职位</text>
      <text x="332" y="355">食物，睡眠</text>
    </g>
    <g font-family="Montserrat, sans-serif" font-size="10" font-weight="700" fill="var(--navy)">
      <text transform="translate(146,222) rotate(-58)" text-anchor="middle">Spiritual Needs</text>
      <text transform="translate(78,322) rotate(-58)" text-anchor="middle">Material Needs</text>
    </g>
    <g fill="none" stroke-width="1.5">
      <circle cx="420" cy="198" r="12" stroke="var(--orange)" stroke-dasharray="3 2"/>
      <path d="M415 193l10 10M425 193l-10 10" stroke="var(--orange)"/>
      <circle cx="420" cy="262" r="12" stroke="var(--navy)" stroke-dasharray="3 2"/>
      <path d="M414 262l4 4 8-8" stroke="var(--orange)"/>
      <circle cx="420" cy="344" r="12" stroke="var(--navy)" stroke-dasharray="3 2"/>
      <path d="M414 344l4 4 8-8" stroke="var(--orange)"/>
      <path d="M420 210v40M420 274v58" stroke="var(--grey-light)" stroke-dasharray="2 3"/>
    </g>
    <g font-family="Montserrat, sans-serif" font-size="9" fill="var(--navy)">
      <text x="440" y="201">Monetary reward</text>
      <text x="440" y="260">Experiential rewards</text>
      <text x="440" y="271">and recognition</text>
      <text x="440" y="347">Monetary reward</text>
    </g>
  </svg>
  <div class="footer-brand">LUMARO . gift</div>
  <div class="page-num">10</div>
</section>

<!-- Trend -->
<section class="slide col-r row-6">
  <div class="navy-panel" style="width:208px"></div>
  <div class="panel-photo" role="img" aria-label="Faint dusk city skyline fading into the navy panel"></div>
  <p class="panel-stat-title">Share of US business using non-cash rewards</p>
  <svg class="diagram" width="208" height="440" viewBox="0 0 208 440" font-family="Montserrat, sans-serif">
    <text x="104" y="170" text-anchor="middle" font-size="13" fill="#dfe4ea">Percent</text>
    <circle cx="104" cy="240" r="44" fill="none" stroke="#8c96a0" stroke-width="13"/>
    <circle cx="104" cy="240" r="44" fill="none" stroke="var(--orange)" stroke-width="13" stroke-dasharray="66.4 276.5" transform="rotate(-90 104 240)"/>
    <text x="140" y="192" font-size="10" fill="var(--orange)">24%</text>
    <text x="36" y="290" font-size="10" fill="#b0b8c0">80%</text>
    <circle cx="64" cy="330" r="3" fill="var(--orange)"/><text x="70" y="333" font-size="8" fill="#dfe4ea">1996</text>
    <circle cx="102" cy="330" r="3" fill="#8c96a0"/><text x="108" y="333" font-size="8" fill="#dfe4ea">2016</text>
  </svg>

  <h2 class="trend-title">Companies are recognizing<br>this trend</h2>
  <p class="trend-sub">Portfolio of Occasions for non-cash rewards</p>

  <svg class="diagram" width="582" height="440" viewBox="0 0 582 440" font-family="Montserrat, sans-serif">
    <g stroke="#fff" stroke-width="3">
      <path d="M350 139.3A84 84 0 0 1 434 139.3L409 182.6A34 34 0 0 0 375 182.6Z" fill="var(--orange)"/>
      <path d="M434 139.3A84 84 0 0 1 476 212L426 212A34 34 0 0 0 409 182.6Z" fill="var(--navy)"/>
      <path d="M476 212A84 84 0 0 1 434 284.7L409 241.4A34 34 0 0 0 426 212Z" fill="var(--orange)"/>
      <path d="M434 284.7A84 84 0 0 1 350 284.7L375 241.4A34 34 0 0 0 409 241.4Z" fill="var(--navy)"/>
      <path d="M350 284.7A84 84 0 0 1 308 212L358 212A34 34 0 0 0 375 241.4Z" fill="var(--orange)"/>
      <path d="M308 212A84 84 0 0 1 350 139.3L375 182.6A34 34 0 0 0 358 212Z" fill="var(--navy)"/>
    </g>
    <g fill="#fff" font-size="8" font-weight="600" text-anchor="middle">
      <text x="392" y="158">Peer to</text><text x="392" y="167">Peer</text>
      <text x="443" y="185">Values</text>
      <text x="443" y="244">New</text><text x="443" y="253">customers</text>
      <text x="392" y="270">Great</text><text x="392" y="279">feedback</text>
      <text x="341" y="244">Strategy</text>
      <text x="341" y="185">Safety</text>
    </g>
  </svg>

  <div class="occasion occasion--right-align" style="left:224px;top:96px;width:118px"><h4>Peer to Peer</h4>Allowing the workplace heroes to be determined by the employees themselves</div>
  <div class="occasion" style="left:482px;top:100px;width:96px"><h4>Values</h4>How your employees are bringing your values to life. The real-life behaviors that make your values what they are</div>
  <div class="occasion occasion--right-align" style="left:218px;top:148px;width:86px"><h4>Safety</h4>Having a safety award can bring the importance of safe workplace practices to the front of everyone's minds</div>
  <div class="occasion" style="left:484px;top:226px;width:96px"><h4>New customers</h4>Whether it is signed contracts, new leads, or when some pays. Recognizing growth is crucial.</div>
  <div class="occasion occasion--right-align" style="left:218px;top:262px;width:86px"><h4>Strategy</h4>If there are specific goals within your business you can run tactical strategic awards to help you achieve them</div>
  <div class="occasion" style="left:436px;top:300px;width:140px"><h4>Great feedback</h4>Great feedback is good for any organisation, taking the pulse and telling you how your employees are impacting your customers</div>
  <div class="page-num" style="right:24px;top:414px">16</div>
</section>

</body>
</html>
```